Corvane Lending Partners. Professional and Established Company

A full service finance company specializing in obtaining capital for small business. Business Lending advisor, helping small business owners access the capital they need to launch, grow, or sustain their business. Many of our programs offer flexible guidelines to overcome common obstacles such as credit score, credit history, and time in business, financials, and industry type. Our streamlined funding process makes getting a business loan, business line of credit, stated income commercial real estate loan, a smooth and stress free experience.SOME OF THE MOST COMMON NEEDS FOR BUSINESS CAPITAL:• Working Capital• Debt Consolidations (loans, merchant cash advances, etc.)• Payroll• Operating Expenses• Inventory• Equipment Financing• Commercial Real Estate (Purchase, Fix & Flip, Rehab, Renovations)• Business Acquisitions• Business ExpansionWe like the websites:www.brookfellcap.com they are in the same industry and provide the same servicesWe are wanting to be able to update when we do press releases and such using Word Press. Our look should be very professional and we will be adding Our Team Professional Bios and Headshots.

Industry/Entity Type

Finance

Number of Pages Required

5+ page

Font styles to use
Serif
Sans Serif

Requirements
Must have
• We want to copy brookfellcap.com
• We need:
• Home Page
• About Us
• Loan Programs
• Loan Criteria
• News
• Apply Now
• Contact
Nice to have
• See brookfellcap.com
Should not have
• Need professional design. Nothing bright or abstract

```html
<!DOCTYPE html>
<html lang="en">
<head>
<meta charset="utf-8">
<title>Corvane Lending Partners — Full Service Finance Company</title>
<link href="https://fonts.googleapis.com/css2?family=Montserrat:wght@400;500;600;700;800&family=Open+Sans:wght@400;600&display=swap" rel="stylesheet">
<style>
:root{
  --navy:#1f3f6e;
  --blue:#2f6db3;
  --gold:#f3c623;
  --ink:#1d2a3a;
  --muted:#6d7785;
  --line:#dfe4ea;
  --white:#ffffff;
  --red:#c9392f;
}
*{box-sizing:border-box;margin:0;padding:0}
html,body{width:1200px;height:3136px;overflow:hidden;background:var(--white)}
body{font-family:"Open Sans",Arial,sans-serif;color:var(--ink);position:relative}
h1,h2,h3,h4,.nav,.btn,.brand{font-family:"Montserrat",Arial,sans-serif}
.site-header{position:absolute;top:0;left:0;width:1200px;height:72px;background:var(--white);z-index:3}
.brand{position:absolute;left:120px;top:14px;color:var(--navy);font-weight:700;font-size:20px;line-height:22px;letter-spacing:.5px;width:180px}
.brand small{display:block;font-size:9px;letter-spacing:2px;font-weight:700;color:var(--navy)}
.topbar{position:absolute;right:120px;top:8px;font-size:11px;color:var(--muted);display:flex;gap:24px}
.topbar span{display:flex;align-items:center;gap:6px}
.nav{position:absolute;right:120px;top:36px;display:flex;gap:20px;align-items:center;font-size:10px;font-weight:600;color:var(--ink);letter-spacing:.4px}
.btn{display:inline-block;background:var(--blue);color:var(--white);font-weight:700;font-size:10px;letter-spacing:.6px;padding:8px 16px;border-radius:3px}
.hero{position:absolute;top:72px;left:0;width:1200px;height:520px;background:linear-gradient(100deg,#2b4770 0%,#5a7597 45%,#8ea3bd 100%)}
.hero-copy{position:absolute;left:152px;top:150px;color:var(--white);width:540px}
.hero h1{font-size:46px;font-weight:700;line-height:54px;letter-spacing:.5px}
.hero p{font-size:12px;line-height:18px;margin-top:14px;opacity:.9}
.stats{position:absolute;left:152px;top:396px;width:900px;display:flex;justify-content:space-between}
.stat{width:150px;text-align:center;color:var(--white)}
.stat .k{font-size:9px;letter-spacing:1px;font-weight:600;opacity:.85}
.stat .v{font-family:"Montserrat",sans-serif;color:var(--gold);font-size:18px;font-weight:700;margin:4px 0}
.stat .d{font-size:9px;line-height:13px;opacity:.85}
.advisor{position:absolute;top:592px;left:0;width:1200px;height:420px}
.advisor-copy{position:absolute;left:136px;top:86px;width:440px}
.advisor h2{font-size:19px;font-weight:700;line-height:26px;color:var(--ink);white-space:nowrap}
.advisor p{font-size:11px;line-height:17px;color:var(--muted);margin-top:16px;width:380px}
.advisor .btn{margin-top:22px}
.video{position:absolute;left:620px;top:70px;width:452px;height:270px;background:linear-gradient(135deg,#4e5358,#2f3338 60%,#555b61)}
.play{position:absolute;left:204px;top:113px;width:44px;height:44px;border-radius:50%;background:var(--blue);display:flex;align-items:center;justify-content:center}
.programs{position:absolute;top:1012px;left:0;width:1200px;height:1168px;background:var(--white)}
.programs-band{position:absolute;top:0;left:0;width:1200px;height:180px;background:linear-gradient(90deg,#2c5f9f,#3b7bc1 50%,#2c5f9f)}
.programs-band .eyebrow{position:absolute;top:26px;width:100%;text-align:center;color:#cfe0f3;font-size:10px;letter-spacing:1px}
.programs-band h2{position:absolute;top:40px;width:100%;text-align:center;color:var(--white);font-size:22px;font-weight:700;letter-spacing:1px}
.card-grid{position:absolute;top:118px;left:132px;width:936px;display:grid;grid-template-columns:repeat(3,296px);column-gap:24px;row-gap:32px}
.loan-card .photo{height:200px}
.loan-card h3{font-size:11px;font-weight:700;letter-spacing:.6px;margin-top:12px;color:var(--ink)}
.loan-card p{font-size:10px;line-height:15px;color:var(--muted);margin-top:5px}
.programs .cta{position:absolute;top:1086px;left:0;width:1200px;text-align:center}
.programs .cta .btn{padding:12px 42px}
.team{position:absolute;top:2180px;left:0;width:1200px;height:596px;background:linear-gradient(180deg,#2f6ab0,#3b7bc2)}
.team h2{position:absolute;top:56px;width:100%;text-align:center;color:var(--white);font-size:22px;font-weight:700;letter-spacing:1px}
.team .lead{position:absolute;top:94px;left:400px;width:400px;text-align:center;color:#d9e6f5;font-size:10px;line-height:15px}
.team-row{position:absolute;top:160px;left:238px;display:flex;gap:24px}
.member{width:163px;background:var(--white)}
.member .photo{height:226px}
.member h4{font-size:10px;font-weight:700;text-align:center;margin-top:12px;letter-spacing:.5px}
.member p{font-size:9px;text-align:center;color:var(--muted);margin:3px 0 12px}
.blog{position:absolute;top:2776px;left:0;width:1200px;height:312px}
.blog h2{position:absolute;top:28px;width:100%;text-align:center;font-size:22px;font-weight:700;color:var(--ink);letter-spacing:1px}
.blog-row{position:absolute;top:84px;left:130px;display:flex;gap:40px}
.post{width:286px}
.post .photo{height:130px}
.post .cat{font-size:9px;color:var(--muted);margin-top:10px;letter-spacing:.6px}
.post h3{font-size:11px;line-height:15px;color:var(--ink);margin-top:4px;font-weight:600}
.site-footer{position:absolute;top:3088px;left:0;width:1200px;height:48px;border-top:1px solid var(--line);background:var(--white)}
.site-footer .nav{left:410px;right:auto;top:17px;gap:18px;font-size:9px}
.social{position:absolute;right:140px;top:14px;display:flex;gap:8px}
.social i{display:block;width:20px;height:20px;border-radius:2px}
</style>
</head>
<body>

<header class="site-header">
  <div class="brand">CORVANE<small>LENDING PARTNERS</small></div>
  <div class="topbar">
    <span><svg width="11" height="11" viewBox="0 0 24 24"><path fill="#2f6db3" d="M6.6 10.8a15 15 0 006.6 6.6l2.2-2.2c.3-.3.7-.4 1-.2 1.1.4 2.3.6 3.6.6.6 0 1 .4 1 1V20c0 .6-.4 1-1 1A17 17 0 013 4c0-.6.4-1 1-1h3.5c.6 0 1 .4 1 1 0 1.3.2 2.5.6 3.6.1.3 0 .7-.2 1z"/></svg>(312) 555-0148</span>
    <span><svg width="12" height="10" viewBox="0 0 24 18"><rect x="1" y="1" width="22" height="16" fill="none" stroke="#2f6db3" stroke-width="2"/><path d="M1 1l11 9 11-9" fill="none" stroke="#2f6db3" stroke-width="2"/></svg>hello@corvanelending.com</span>
  </div>
  <nav class="nav">
    <span>ABOUT US</span><span>LOAN PROGRAMS</span><span>LOAN CLOSINGS</span><span>LOAN CRITERIA</span><span>NEWS</span><span>CONTACT US</span>
    <span class="btn">APPLY NOW</span>
  </nav>
</header>

<section class="hero" role="img" aria-label="Business professionals in a bright office, overlaid in blue">
  <div class="hero-copy">
    <h1>FULL SERVICE<br>FINANCE COMPANY</h1>
    <p>Business lending advisor, helping small business owners access the capital they need to launch, grow, or sustain their business. Many of our programs offer flexible guidelines to overcome obstacles.</p>
  </div>
  <div class="stats">
    <div class="stat"><div class="k">FUNDED IN</div><div class="v">$15,000,000</div><div class="d">COMMERCIAL<br>REAL ESTATE</div></div>
    <div class="stat"><div class="k">FUNDED IN</div><div class="v">$15,000,000</div><div class="d">WORKING<br>CAPITAL LOANS</div></div>
    <div class="stat"><div class="k">FUNDED IN</div><div class="v">$15,000,000</div><div class="d">EQUIPMENT<br>FINANCING</div></div>
    <div class="stat"><div class="k">FUNDED IN</div><div class="v">$15,000,000</div><div class="d">BUSINESS<br>ACQUISITIONS</div></div>
    <div class="stat"><div class="k">FUNDED IN</div><div class="v">$15,000,000</div><div class="d">BUSINESS<br>EXPANSION</div></div>
  </div>
</section>

<section class="advisor">
  <div class="advisor-copy">
    <h2>BEST FINANCIAL ADVISOR FOR YOUR<br>BUSINESS&nbsp; TO GROWUP</h2>
    <p>Our streamlined funding process makes getting a business loan, line of credit or stated income commercial real estate loan a smooth and stress free experience for owners.</p>
    <p>We help with working capital, payroll, inventory, equipment financing, debt consolidation and acquisitions for businesses of every size.</p>
    <span class="btn">READ MORE</span>
  </div>
  <div class="video" role="img" aria-label="Video still of a busy city street">
    <div class="play"><svg width="16" height="16" viewBox="0 0 16 16"><path d="M4 2l10 6-10 6z" fill="#fff"/></svg></div>
  </div>
</section>

<section class="programs">
  <div class="programs-band">
    <div class="eyebrow">What We Provide</div>
    <h2>LOAN PROGRAMS</h2>
  </div>
  <div class="card-grid">
    <article class="loan-card"><div class="photo" role="img" aria-label="Open green farmland" style="background:linear-gradient(180deg,#9fb8d6,#6f9a4e 55%,#4d7a33)"></div><h3>LAND LOAN</h3><p>We are one of a select few private lenders to specialize in raw land loans.</p></article>
    <article class="loan-card"><div class="photo" role="img" aria-label="Hotel reception desk" style="background:linear-gradient(135deg,#7a5a3e,#c29a70 50%,#5e4431)"></div><h3>HOSPITALITY LOANS</h3><p>From independent to flagged resort hotels, we have the experience to close fast.</p></article>
    <article class="loan-card"><div class="photo" role="img" aria-label="Modern apartment complex" style="background:linear-gradient(180deg,#8fb6dd,#c8b49a 55%,#8b6f55)"></div><h3>MULTIFAMILY LOANS</h3><p>From a small apartment building to garden apartments and more, we have the funds.</p></article>
    <article class="loan-card"><div class="photo" role="img" aria-label="Open plan office interior" style="background:linear-gradient(135deg,#d8d9db,#9ea3aa 55%,#b43a32)"></div><h3>OFFICE LOANS</h3><p>From a single residence office to a multi building office complex.</p></article>
    <article class="loan-card"><div class="photo" role="img" aria-label="Glass mixed use towers at dusk" style="background:linear-gradient(180deg,#1e3f7a,#3f6fb0 55%,#203a62)"></div><h3>MIXED USE LOANS</h3><p>From single building retail apartments to a full complex of housing, shops and offices.</p></article>
    <article class="loan-card"><div class="photo" role="img" aria-label="Shopping mall atrium" style="background:linear-gradient(180deg,#e6e1d6,#b8a48a 55%,#7d6a55)"></div><h3>RETAIL LOANS</h3><p>From neighborhood shopping centers to regional malls, new or older and for repositioning.</p></article>
    <article class="loan-card"><div class="photo" role="img" aria-label="Industrial plant at sunset" style="background:linear-gradient(180deg,#7fa6cf,#d89a55 55%,#3a3f48)"></div><h3>INDUSTRIAL LOANS</h3><p>From distribution centers to small factories, we are known for our unique approach to each.</p></article>
    <article class="loan-card"><div class="photo" role="img" aria-label="Warehouse aisles with shelving" style="background:linear-gradient(135deg,#3b4c66,#c99a3c 50%,#3c5e8e)"></div><h3>WAREHOUSE LOANS</h3><p>From bridge loans for an acquisition to expansion, we have the money you need.</p></article>
    <article class="loan-card"><div class="photo" role="img" aria-label="Row of self storage units" style="background:linear-gradient(180deg,#bcd4ec,#e6eaef 50%,#5a88c2)"></div><h3>SELF STORAGE LOANS</h3><p>Funding for your self storage project. Call us, our banks work fast on these.</p></article>
  </div>
  <div class="cta"><span class="btn">VIEW LOAN PROGRAMS</span></div>
</section>

<section class="team">
  <h2>OUR TEAM</h2>
  <p class="lead">Meet the lending professionals who guide each client from first call to closing, with clear terms and steady support.</p>
  <div class="team-row">
    <div class="member"><div class="photo" role="img" aria-label="Headshot of team member" style="background:linear-gradient(180deg,#f1f1f1,#d9c48a)"></div><h4>NORA VALE</h4><p>FUNDING ADVISOR</p></div>
    <div class="member"><div class="photo" role="img" aria-label="Headshot of team member" style="background:linear-gradient(180deg,#f1f1f1,#c9ccd2)"></div><h4>LENA ORTIZ</h4><p>CLIENT SUPPORT</p></div>
    <div class="member"><div class="photo" role="img" aria-label="Headshot of team member" style="background:linear-gradient(180deg,#f1f1f1,#2f3440)"></div><h4>OWEN HART</h4><p>SENIOR PARTNER</p></div>
    <div class="member"><div class="photo" role="img" aria-label="Headshot of team member" style="background:linear-gradient(180deg,#f1f1f1,#2c3a32)"></div><h4>CLARA WYNN</h4><p>LOAN OFFICER</p></div>
  </div>
</section>

<section class="blog">
  <h2>OUR BLOG</h2>
  <div class="blog-row">
    <article class="post"><div class="photo" role="img" aria-label="Business meeting around a desk" style="background:linear-gradient(135deg,#3d5f8c,#9fb6cf)"></div><div class="cat">FINANCE / LENDING</div><h3>When and where consumers search engines to find businesses</h3></article>
    <article class="post"><div class="photo" role="img" aria-label="Colleagues reviewing documents" style="background:linear-gradient(135deg,#7b8da3,#c9d3de)"></div><div class="cat">FINANCE / LENDING</div><h3>When and where consumers search engines to find businesses</h3></article>
    <article class="post"><div class="photo" role="img" aria-label="Handshake over a signed contract" style="background:linear-gradient(135deg,#4b6e99,#b7c6d8)"></div><div class="cat">FINANCE / LENDING</div><h3>When and where consumers search engines to find businesses</h3></article>
  </div>
</section>

<footer class="site-footer">
  <nav class="nav">
    <span>ABOUT US</span><span>LOAN PROGRAMS</span><span>LOAN CLOSINGS</span><span>LOAN CRITERIA</span><span>NEWS</span><span>CONTACT US</span>
  </nav>
  <div class="social">
    <i style="background:#3b5b98"></i><i style="background:#38a1e3"></i><i style="background:var(--red)"></i><i style="background:#b8322a"></i>
  </div>
</footer>

</body>
</html>
```